Home page design for a live auction website.

Hi, we are looking at finding a good design for an auction website, only home page .. We will not be selling anything online, so the website will only be a portal where visitors can check about our company, upcoming auctions, online catalogues etc.
See attached our logo. Please use the same red that you see on the logo in the designs that you provide.
The final design should communicate high-end auction website, as we will be selling expensive piece of arts and antiques.
We should have a main frame where images of arts will circulate, with description of the art piece. just like on http://paris.velmontrade-crespel.com/
(but with a better design overall) and of course a menu with different tabs, like "about us", "previous sales" "next sales", "contact" , "how to buy", "meet our specialists".

Target Market(s)

High end segment, who can afford to pay up to 250'000 for a piece of art

Industry/Entity Type

Online

Number of Pages Required

1 page

Requirements
Must have
• a frame with images rotating, just like on http://paris.velmontrade-crespel.com/ . but the rest of the design should be more refined.
• we should also have a strong call to action, "Free online estimation", click here, estimation delivered in 48 hours"
Nice to have
• Halvery Auctions, the brand should be well visible

```html
<!DOCTYPE html>
<html lang="en">
<head>
<meta charset="utf-8">
<title>Halvery Auctions</title>
<link href="https://fonts.googleapis.com/css2?family=Open+Sans:wght@300;400;600;700&display=swap" rel="stylesheet">
<style>
:root{
  --red:#b8161c;
  --red-dark:#8f0f14;
  --ink:#2b2b2b;
  --dark:#2e2e2e;
  --darker:#1d1d1d;
  --band:#3a3a3a;
  --grey:#ececec;
  --line:#d6d6d6;
  --muted:#777;
  --white:#fff;
}
*{margin:0;padding:0;box-sizing:border-box}
html,body{width:1200px;height:2404px;overflow:hidden}
body{font-family:'Open Sans',sans-serif;color:var(--ink);background:#f4f4f4;position:relative;font-size:11px}
.abs{position:absolute}
.topbar{left:0;top:0;width:1200px;height:32px;background:var(--darker);color:#bbb;font-size:10px}
.topbar .contact{left:112px;top:4px;line-height:12px}
.topbar .social{right:112px;top:8px;display:flex;gap:4px}
.social span{width:16px;height:16px;background:#555;display:block}
.social span.r{background:var(--red)}
.header{left:0;top:32px;width:1200px;height:118px;background:var(--white)}
.brand{left:0;width:1200px;top:22px;text-align:center}
.brand .mark{width:48px;height:48px;background:var(--red);margin:0 auto 8px}
.brand .name{font-size:13px;font-weight:600;letter-spacing:3px;color:var(--red);text-transform:uppercase}
.nav{left:0;top:150px;width:1200px;height:32px;background:var(--red)}
.nav ul{list-style:none;display:flex;justify-content:center;gap:0;height:32px;align-items:center}
.nav li{color:#fff;font-size:10px;font-weight:600;text-transform:uppercase;padding:0 14px;line-height:32px}
.nav li.active{background:var(--red-dark)}
.nav .search{right:112px;top:9px}
.hero{left:80px;top:196px;width:1040px;height:330px}
.hero .photo{left:0;top:0;width:700px;height:330px;background:linear-gradient(135deg,#7b6c55,#3b342a 55%,#a89779)}
.hero .caption{left:0;bottom:0;width:700px;height:40px;background:rgba(0,0,0,.75);color:#fff;font-size:9px;font-weight:700;padding:8px 14px;text-transform:uppercase}
.hero .caption .price{position:absolute;right:14px;top:14px;color:#fff}
.hero .panel{left:700px;top:0;width:340px;height:330px;background:var(--red);color:#fff;padding:20px 24px;font-size:11px;line-height:15px}
.hero .panel .box{margin-top:24px;background:#fff;color:var(--ink);padding:12px 14px;font-size:10px;line-height:14px}
.hero .panel .box b{color:var(--red);display:block}
.arrow{top:330px}
.featured .title{left:0;top:580px;width:1200px;text-align:center;color:#fff;font-size:26px;font-weight:300}
.cards{left:112px;top:640px;display:flex;gap:24px}
.card{width:176px;background:#fff}
.card .img{height:150px}
.card .label{background:var(--red);color:#fff;font-size:9px;font-weight:700;text-transform:uppercase;padding:6px 8px;line-height:12px;height:38px}
.card .price{color:var(--ink);font-size:10px;font-weight:600;padding:6px 8px}
.past h2{font-size:16px;font-weight:400;color:var(--red);position:absolute}
.evt{display:flex;gap:12px;margin-bottom:16px}
.evt .img{width:96px;height:72px;flex:none}
.evt h3{font-size:10px;font-weight:700;line-height:13px}
.evt p{font-size:9px;color:var(--muted);line-height:12px;margin-top:3px}
.evt .p{color:var(--red);font-weight:700;font-size:9px;margin-top:3px}
.big h3{font-size:11px;font-weight:700;color:var(--red);margin-top:10px}
.big p{font-size:9px;color:var(--muted);line-height:13px;margin-top:4px}
.tabs{left:112px;top:1460px;width:976px;height:32px;background:var(--grey);display:flex}
.tabs span{padding:0 16px;line-height:32px;font-size:10px;color:#444}
.tabs span.on{background:var(--red);color:#fff}
.toolbar{left:112px;top:1500px;width:976px;height:28px;border-bottom:1px solid var(--line);font-size:10px;color:var(--muted)}
.select{border:1px solid var(--line);background:#fff;padding:2px 8px;width:70px;display:inline-block;margin-left:6px}
.grid{left:112px;top:1550px;width:976px;display:grid;grid-template-columns:repeat(5,176px);column-gap:24px;row-gap:24px}
.item .img{height:150px}
.item h4{font-size:10px;font-weight:600;margin-top:6px}
.item .p{font-size:9px;color:var(--red);font-weight:700;margin-top:2px}
.more{left:560px;top:2062px;width:80px;height:22px;background:var(--red);color:#fff;font-size:9px;font-weight:700;text-align:center;line-height:22px}
.footer{left:0;top:2110px;width:1200px;height:258px;background:var(--dark);color:#aaa}
.footer h5{color:#fff;font-size:10px;font-weight:700;text-transform:uppercase;margin-bottom:12px}
.footer ul{list-style:none;font-size:9px;line-height:18px}
.footer li::before{content:"› ";color:var(--red)}
.footer .col{position:absolute;top:28px}
.footer .input{width:200px;height:22px;background:#fff;margin-bottom:8px}
.footer .btn{width:52px;height:18px;background:var(--red);color:#fff;font-size:8px;text-align:center;line-height:18px}
.footer .circles{display:flex;gap:6px;margin-top:12px}
.footer .circles span{width:18px;height:18px;border-radius:50%;background:#555}
.footer .circles span.r{background:var(--red)}
.bottom{left:0;top:2368px;width:1200px;height:36px;background:var(--darker);color:#888;font-size:9px}
.bottom .copy{left:112px;top:12px}
.bottom .links{right:112px;top:12px;display:flex;gap:14px;text-transform:uppercase}
</style>
</head>
<body>

<div class="topbar abs">
  <div class="contact abs">+41 555 010 2040<br>info@halveryauctions.com</div>
  <div class="social abs"><span class="r"></span><span></span><span></span><span></span></div>
</div>

<header class="header abs">
  <div class="brand abs">
    <div class="mark"></div>
    <div class="name">Halvery Auctions</div>
  </div>
</header>

<nav class="nav abs">
  <ul>
    <li class="active">Home</li><li>About Us</li><li>Previous Sales</li><li>Next Sales</li><li>Contact</li><li>How To Buy</li><li>Meet Our Specialists</li>
  </ul>
  <svg class="search abs" width="14" height="14" viewBox="0 0 14 14"><circle cx="6" cy="6" r="4.5" fill="none" stroke="#fff" stroke-width="1.6"/><line x1="9.5" y1="9.5" x2="13" y2="13" stroke="#fff" stroke-width="1.6"/></svg>
</nav>

<svg class="abs arrow" style="left:40px" width="20" height="40" viewBox="0 0 20 40"><polyline points="16,2 4,20 16,38" fill="none" stroke="#999" stroke-width="2"/></svg>
<svg class="abs arrow" style="right:40px" width="20" height="40" viewBox="0 0 20 40"><polyline points="4,2 16,20 4,38" fill="none" stroke="#999" stroke-width="2"/></svg>

<section class="hero abs">
  <div class="photo abs" role="img" aria-label="Antique vintage camera lenses featured lot"></div>
  <div class="caption abs">Quisque eget odio ac lectus vestibulum faucibus eget in<br>metus. In pellentesque faucibus vestibulum<span class="price">$20000 - $40000</span></div>
  <div class="panel abs">
    Mauris iaculis porttitor posuere. Praesent id metus massa, ut blandit odio. Proin quis tortor orci. Etiam at risus et justo dignissim congue. Donec congue lacinia dui, a porttitor lectus condimentum laoreet. Nunc eu ullamcorper orci.
    <div class="box">
      <b>Quisque Eget Odio Ac Lectus</b>
      Faucibus Eget In Metus<br><br>
      Address line 1, Address line 2,<br>Phone: 0123456789<br>info@halveryauctions.com
    </div>
  </div>
</section>

<svg class="abs" style="left:0;top:530px" width="1200" height="490" viewBox="0 0 1200 490"><path d="M0 60 Q600 -40 1200 60 V490 H0 Z" fill="#3a3a3a"/></svg>

<section class="featured">
  <h2 class="title abs">Featured Auction</h2>
  <div class="cards abs">
    <div class="card"><div class="img" role="img" aria-label="Vintage radio" style="background:linear-gradient(#d9c6a0,#7a5a34)"></div><div class="label">Praesent Id Metus<br>Massa, Ut Blandit</div><div class="price">$15000 - $20000</div></div>
    <div class="card"><div class="img" role="img" aria-label="Antique telephone" style="background:linear-gradient(#cfcfcf,#4a4a4a)"></div><div class="label">Praesent Id Metus<br>Massa, Ut Blandit</div><div class="price">$15000 - $20000</div></div>
    <div class="card"><div class="img" role="img" aria-label="Green glass vase" style="background:linear-gradient(#8fbf6a,#2f5e22)"></div><div class="label">Praesent Id Metus<br>Massa, Ut Blandit</div><div class="price">$15000 - $20000</div></div>
    <div class="card"><div class="img" role="img" aria-label="Vintage camera" style="background:linear-gradient(#b59a72,#3c2e22)"></div><div class="label">Praesent Id Metus<br>Massa, Ut Blandit</div><div class="price">$15000 - $20000</div></div>
    <div class="card"><div class="img" role="img" aria-label="Antique wooden chest" style="background:linear-gradient(#a57445,#4a2c16)"></div><div class="label">Praesent Id Metus<br>Massa, Ut Blandit</div><div class="price">$15000 - $20000</div></div>
  </div>
</section>

<section class="past">
  <h2 style="left:112px;top:1040px">Past Events</h2>
  <div class="abs" style="left:112px;top:1074px;width:460px">
    <div class="evt"><div class="img" role="img" aria-label="Antique pocket watch" style="background:linear-gradient(#c9a46a,#5c4020)"></div><div><h3>Nulla At Nulla Justo, Eget Luctus Tortor, Quisq Eget Odio Ac Lectus</h3><p>11 Sep 2015<br>Lorem ipsum dolor sit amet, adipiscing elit. Nullam et ut ultricies. Vivamus hendrerit.</p><div class="p">$900 - $1500</div></div></div>
    <div class="evt"><div class="img" role="img" aria-label="Brass telescope" style="background:linear-gradient(#e0cfa8,#7a6238)"></div><div><h3>Nulla At Nulla Justo, Eget Luctus Tortor, Quisq Eget Odio Ac Lectus</h3><p>11 Sep 2015<br>Lorem ipsum dolor sit amet, adipiscing elit. Nullam et ut ultricies. Vivamus hendrerit.</p><div class="p">$900 - $1500</div></div></div>
    <div class="evt"><div class="img" role="img" aria-label="Antique clock" style="background:linear-gradient(#9a5a3a,#3a1e12)"></div><div><h3>Nulla At Nulla Justo, Eget Luctus Tortor, Quisq Eget Odio Ac Lectus</h3><p>11 Sep 2015<br>Lorem ipsum dolor sit amet, adipiscing elit. Nullam et ut ultricies. Vivamus hendrerit.</p><div class="p">$900 - $1500</div></div></div>
  </div>
  <h2 style="left:620px;top:1040px">Past Events</h2>
  <div class="abs big" style="left:620px;top:1074px;width:468px">
    <div role="img" aria-label="Vintage stamps and postage collection" style="height:190px;background:linear-gradient(135deg,#6e4b3a,#b23a2a 50%,#3b2a22)"></div>
    <h3>Nulla At Nulla Justo, Eget Luctus Tortor, Quisq Eget Odio Ac Lectus</h3>
    <p>11 Sep 2015</p>
    <p>Duis aliquet aliquam purus at hendrerit. Vestibulum vulputate, ligula lacinia consectetur, lacus lorem ornare metus, vel egestas erat ut erat ipsum. Donec auctor lacus commodo eros porta.</p>
    <div style="color:var(--red);font-weight:700;font-size:9px;margin-top:4px">$900 - $1500</div>
  </div>
</section>

<div class="tabs abs"><span class="on">All</span><span>Asian Antiquities</span><span>Jewelry</span><span>Collectibles</span><span>Furniture</span><span>Home &amp; Garden</span><span>Fashion</span><span>Other</span></div>
<div class="toolbar abs">
  <span class="abs" style="left:0;top:6px">1036 Events</span>
  <span class="abs" style="right:0;top:2px"><span class="select">Sort By</span><span class="select">View 20</span></span>
</div>

<section class="grid abs">
  <div class="item"><div class="img" role="img" aria-label="Silver teapot" style="background:linear-gradient(#e6e2da,#8a8378)"></div><h4>Praesent Id Metus Massa</h4><div class="p">$15000 - $20000</div></div>
  <div class="item"><div class="img" role="img" aria-label="Framed portrait painting" style="background:linear-gradient(#c7b48c,#3d3320)"></div><h4>Praesent Id Metus Massa</h4><div class="p">$15000 - $20000</div></div>
  <div class="item"><div class="img" role="img" aria-label="Antique oil lamp" style="background:linear-gradient(#d7c8ae,#6b5a3e)"></div><h4>Praesent Id Metus Massa</h4><div class="p">$15000 - $20000</div></div>
  <div class="item"><div class="img" role="img" aria-label="Wooden cabinet" style="background:linear-gradient(#9c6a44,#3e2414)"></div><h4>Praesent Id Metus Massa</h4><div class="p">$15000 - $20000</div></div>
  <div class="item"><div class="img" role="img" aria-label="Ornate mirror" style="background:linear-gradient(#c8a670,#5a3f1c)"></div><h4>Praesent Id Metus Massa</h4><div class="p">$15000 - $20000</div></div>
  <div class="item"><div class="img" role="img" aria-label="Brass candlesticks" style="background:linear-gradient(#cdbb8a,#5e4d26)"></div><h4>Praesent Id Metus Massa</h4><div class="p">$15000 - $20000</div></div>
  <div class="item"><div class="img" role="img" aria-label="Antique carved table" style="background:linear-gradient(#7d4a2c,#2c160c)"></div><h4>Praesent Id Metus Massa</h4><div class="p">$15000 - $20000</div></div>
  <div class="item"><div class="img" role="img" aria-label="Vintage interior room" style="background:linear-gradient(#c59a62,#5a3820)"></div><h4>Praesent Id Metus Massa</h4><div class="p">$15000 - $20000</div></div>
  <div class="item"><div class="img" role="img" aria-label="Antique gramophone" style="background:linear-gradient(#d8cfc2,#6e655a)"></div><h4>Praesent Id Metus Massa</h4><div class="p">$15000 - $20000</div></div>
  <div class="item"><div class="img" role="img" aria-label="Stacked vintage suitcases" style="background:linear-gradient(#a9764c,#4a2e1a)"></div><h4>Praesent Id Metus Massa</h4><div class="p">$15000 - $20000</div></div>
</section>

<div class="more abs">LOAD MORE</div>

<footer class="footer abs">
  <div class="col" style="left:112px">
    <h5>Featured Links</h5>
    <ul><li>Ut enim ad minim veniam</li><li>Duis aute irure dolor</li><li>Excepteur sint occaecat</li><li>Sed ut perspiciatis unde</li><li>Nemo enim ipsam voluptas</li></ul>
  </div>
  <div class="col" style="left:300px;top:50px">
    <ul><li>Ut enim ad minim veniam</li><li>Duis aute irure dolor</li><li>Excepteur sint occaecat</li><li>Sed ut perspiciatis unde</li></ul>
  </div>
  <div class="col" style="left:500px">
    <h5>Contact Info</h5>
    <div style="font-size:9px;line-height:16px">
      <svg width="10" height="12" viewBox="0 0 10 12"><path d="M5 0a4 4 0 0 1 4 4c0 3-4 8-4 8S1 7 1 4a4 4 0 0 1 4-4z" fill="#b8161c"/></svg> Address line 1<br>&nbsp;&nbsp;&nbsp;Address line 2<br>
      <svg width="10" height="10" viewBox="0 0 10 10"><rect x="2" y="0" width="6" height="10" rx="1" fill="#b8161c"/></svg> Phone: +41 555 010 2040<br>
      <svg width="10" height="8" viewBox="0 0 10 8"><rect width="10" height="8" fill="#b8161c"/></svg> info@halveryauctions.com
    </div>
  </div>
  <div class="col" style="left:820px">
    <h5>Join Our Mailing List</h5>
    <div class="input"></div>
    <div class="btn">SUBMIT</div>
    <div class="circles"><span class="r"></span><span></span><span></span><span></span><span></span></div>
  </div>
</footer>

<div class="bottom abs">
  <div class="copy abs">© 2015. All Rights Reserved</div>
  <div class="links abs"><span>Home</span><span>About Us</span><span>Maintenance Service</span><span>Cleaning Tips</span><span>Free Quotes</span><span>Contact</span></div>
</div>

</body>
</html>
```